Brisk Lark Delivery Service Wordpress design

My client is a delivery service whose motto is "We go where the freight leads us." Their colors are red, white and blue. They use Voyara vans and box vans - NO semi tractors. They like this Website design www.kwuzo.com, but I would like to see some designs that make them stand out. Attached is their new logo.

Target Market(s)

Businesses who use delivery services in town and anyone needing freight picked up or transported in the United States.

Industry/Entity Type

Delivery Service

Number of Pages Required

1 page

Font styles to use
Sans Serif

Colors
ec1f27
0455a3
ffffff

Requirements
Must have
• We need a Wordpress design with sliders that incorporates their new logo and the motto "WE GO WHERE THE FREIGHT LEADS US" Their corporate colors are red, white and blue. They only use voyara vans and box vans.
Nice to have
• Please use your creativity to come up with a unique design for this delivery service.
Should not have
• NO SEMI TRACTOR TRAILERS

```html
<!DOCTYPE html>
<html lang="en">
<head>
<meta charset="utf-8">
<title>Brisk Lark Express Delivery</title>
<link href="https://fonts.googleapis.com/css2?family=Lato:wght@400;700;900&display=swap" rel="stylesheet">
<style>
:root{
  --red:#ec1f27;
  --navy:#1f1a6b;
  --ink:#333;
  --body:#444;
  --light:#eeeeee;
  --footer:#333333;
  --footer-deep:#262626;
  --white:#fff;
}
*{box-sizing:border-box;margin:0;padding:0}
html,body{width:1200px;height:2169px;overflow:hidden}
body{font-family:'Lato',sans-serif;color:var(--ink);background:var(--white);position:relative}
ul{list-style:none}

/* header */
.site-header{position:absolute;top:0;left:0;width:1200px;height:87px}
.brand{position:absolute;left:133px;top:20px;display:flex;align-items:center;gap:12px}
.brand-mark{width:46px;height:46px;border-radius:50%;background:var(--navy)}
.brand-name{font-weight:900;font-size:27px;color:var(--navy);letter-spacing:.5px;line-height:1}
.hotline{position:absolute;right:130px;top:22px;display:flex;align-items:center;gap:8px}
.hotline small{display:block;font-size:11px;color:var(--ink)}
.hotline strong{display:block;font-size:24px;color:var(--navy);font-weight:700;line-height:1.05}

.main-nav{position:absolute;top:87px;left:0;width:1200px;height:43px;background:var(--red)}
.main-nav ul{position:absolute;left:133px;display:flex;height:43px}
.main-nav a{display:block;height:43px;line-height:43px;color:var(--white);font-size:13px;text-transform:uppercase;text-decoration:none}
.main-nav li:first-child a{background:var(--navy);padding:0 23px}
.main-nav li+li a{margin-left:47px}
.main-nav li:nth-child(2) a{margin-left:19px}

/* hero */
.hero{position:absolute;top:130px;left:0;width:1200px;height:477px;background:linear-gradient(90deg,#b9cbe0 0%,#e6dccb 30%,#d9c7a8 50%,#c9a98a 65%,#aebcd2 100%)}
.hero-line{position:absolute;left:133px;background:rgba(48,42,120,.85);color:var(--white);font-weight:700;font-size:36px;padding:0 10px;height:44px;line-height:44px;text-transform:uppercase}
.hero-line.one{top:266px}
.hero-line.two{top:312px}

/* about */
.about{position:absolute;top:607px;left:0;width:1200px;height:323px}
.kicker{font-size:21px;color:var(--ink);font-weight:400}
.title{font-size:25px;font-weight:700;color:var(--navy);text-transform:uppercase}
.about .kicker{position:absolute;left:133px;top:43px}
.about .title{position:absolute;left:133px;top:72px}
.about-copy{position:absolute;left:133px;top:115px;width:585px;font-size:14px;line-height:25px;color:var(--body)}
.about-copy p+p{margin-top:8px}
.about-van{position:absolute;left:760px;top:58px;width:310px;height:220px;border-radius:6px;background:linear-gradient(180deg,#f4f4f6,#d9dbe3)}

/* services */
.services{position:absolute;top:930px;left:0;width:1200px;height:467px;background:var(--light);text-align:center}
.services .kicker{position:absolute;left:0;width:1200px;top:30px}
.services .title{position:absolute;left:0;width:1200px;top:58px}
.cards{position:absolute;left:131px;top:128px;display:flex;gap:43px}
.card{width:284px;height:297px;background:var(--white);text-align:left;box-shadow:0 1px 3px rgba(0,0,0,.12);position:relative}
.card-photo{height:198px}
.card:nth-child(1) .card-photo{background:linear-gradient(135deg,#e8e6e2,#2b3c6e 60%,#c2a27a)}
.card:nth-child(2) .card-photo{background:linear-gradient(135deg,#7f96b3,#c9ab83 55%,#e3d9c9)}
.card:nth-child(3) .card-photo{background:linear-gradient(180deg,#8f99a4,#e9ebee 55%,#6f6d6a)}
.card h3{font-size:18px;font-weight:400;color:var(--navy);margin:14px 0 0 18px}
.card h3 span{color:var(--red)}
.card p{font-size:13px;line-height:20px;color:var(--ink);margin:8px 0 0 18px;width:225px}
.card svg{position:absolute;right:16px;bottom:12px}

/* band */
.band{position:absolute;top:1397px;left:0;width:1200px;height:86px}
.band svg.bg{position:absolute;left:0;top:0}
.band-new{position:absolute;left:131px;top:14px;color:var(--white)}
.band-new strong{display:block;font-size:23px;font-weight:400}
.band-new small{font-size:12px}
.band-track{position:absolute;left:500px;top:24px;color:var(--white)}
.band-track small{display:block;font-size:12px}
.band-track strong{font-size:23px;font-weight:400}
.band-actions{position:absolute;right:130px;top:29px;display:flex;align-items:center;gap:14px;color:var(--white);font-size:14px}
.band-actions .or{color:#8f8cb8}
.btn-login{background:var(--red);color:var(--white);height:30px;padding:0 18px;display:flex;align-items:center;gap:6px;font-size:14px}

/* careers + testimonials */
.section-h{font-size:24px;font-weight:400;color:var(--navy)}
.section-h b{font-weight:700}
.careers{position:absolute;left:133px;top:1515px;width:450px}
.careers ul{margin-top:26px}
.careers li{position:relative;padding-left:28px;font-size:14px;line-height:25px;color:var(--ink)}
.careers li svg{position:absolute;left:0;top:6px}
.testimonials{position:absolute;left:623px;top:1515px;width:447px}
.quote{position:relative;margin-top:26px;padding-left:60px;font-size:14px;line-height:25px;color:var(--ink)}
.quote svg{position:absolute;left:0;top:6px}
.author{margin-top:20px;border-top:1px solid #ddd;padding-top:4px;position:relative;height:80px}
.author-photo{position:absolute;left:18px;top:-3px;width:80px;height:80px;border-radius:50%;background:linear-gradient(135deg,#caa88e,#6d5a4f)}
.author-name{position:absolute;left:112px;top:20px;font-size:17px;font-weight:700;color:var(--red)}
.author-place{position:absolute;left:112px;top:45px;font-size:12px}
.author-nav{position:absolute;right:0;top:24px;display:flex;gap:14px}

/* footer */
.site-footer{position:absolute;top:1826px;left:0;width:1200px;height:289px;background:var(--footer);color:#aaa}
.site-footer h4{font-size:18px;font-weight:400;color:var(--white)}
.f-col{position:absolute;top:50px}
.f-links{left:133px}
.f-links ul{margin-top:14px}
.f-links li{font-size:13px;line-height:26px}
.f-news{left:269px;width:230px}
.f-news p{font-size:12px;line-height:23px;margin-top:14px}
.f-news .field{margin-top:16px;background:var(--white);color:#333;font-size:12px;height:33px;line-height:33px;padding-left:13px;width:211px}
.f-news .submit{margin-top:11px;background:var(--red);color:var(--white);font-size:15px;font-weight:700;width:109px;height:33px;line-height:33px;text-align:center}
.f-contact{left:543px;width:200px}
.f-contact p{font-size:13px;line-height:24px;margin-top:14px}
.f-contact p+p{margin-top:9px}
.socials{display:flex;gap:11px;margin-top:14px}
.socials span{width:29px;height:29px;display:block}
.f-map{left:758px;top:53px;width:311px;height:168px;background:linear-gradient(135deg,#b9d8e8,#e7e3d4 45%,#cfe0b9 70%,#b9d8e8)}
.f-map-link{position:absolute;left:758px;top:232px;font-size:12px;color:#aaa;text-decoration:underline}
.legal{position:absolute;top:2115px;left:0;width:1200px;height:54px;background:var(--footer-deep);color:#bbb;font-size:13px}
.legal .copy{position:absolute;left:131px;top:19px}
.legal .links{position:absolute;right:130px;top:19px}
</style>
</head>
<body>

<header class="site-header">
  <div class="brand"><span class="brand-mark"></span><span class="brand-name">BRISK LARK</span></div>
  <div class="hotline">
    <svg width="34" height="34" viewBox="0 0 34 34"><circle cx="17" cy="17" r="16" fill="var(--navy)"/><path d="M11 9c1 0 3 4 3 5s-2 2-2 3c1 2 3 4 5 5 1 0 2-2 3-2s5 2 5 3c0 2-2 4-4 4C14 27 7 20 7 13c0-2 2-4 4-4z" fill="#fff"/></svg>
    <div><small>Respond in 24 hours</small><strong>123 456 7890</strong></div>
  </div>
</header>

<nav class="main-nav">
  <ul>
    <li><a href="#">Home</a></li>
    <li><a href="#">About Us</a></li>
    <li><a href="#">Freight</a></li>
    <li><a href="#">Courier</a></li>
    <li><a href="#">Transported</a></li>
    <li><a href="#">Contact Us</a></li>
    <li><a href="#">Careers</a></li>
    <li><a href="#">Customer Login</a></li>
  </ul>
</nav>

<section class="hero" role="img" aria-label="Courier in a cap handing a parcel box to a customer at a doorway">
  <div class="hero-line one">We go where</div>
  <div class="hero-line two">The freight leads us</div>
</section>

<section class="about">
  <h2 class="kicker">About Us</h2>
  <h1 class="title">Brisk Lark Express Delivery</h1>
  <div class="about-copy">
    <p>Lorem Ipsum is simply dummy text of the printing and typesetting industry. Lorem Ipsum has been the industry's standard dummy text ever since the when an unknown printer took a galley of type and scrambled it to make a type specimen book. It has survived not only five centuries, but also the leap into electronic typesetting, remaining essentially unchanged.</p>
    <p>It was popularised in the with the release of Letraset sheets containing Lorem Ipsum passages, and more recently with desktop publishing software including versions of Lorem Ipsum.</p>
  </div>
  <div class="about-van" role="img" aria-label="White delivery van with a driver holding a parcel"></div>
</section>

<section class="services">
  <h2 class="kicker">Our Service</h2>
  <h2 class="title">Choose a Service Division</h2>
  <div class="cards">
    <article class="card">
      <div class="card-photo" role="img" aria-label="Courier carrying boxes from a van"></div>
      <h3><span>Express</span> Courier</h3>
      <p>Simply dummy text of the printing and typesetting industry.</p>
      <svg width="18" height="14" viewBox="0 0 18 14"><path d="M1 7h15M10 1l6 6-6 6" stroke="var(--red)" stroke-width="2" fill="none"/></svg>
    </article>
    <article class="card">
      <div class="card-photo" role="img" aria-label="Delivery worker with clipboard and stacked parcels"></div>
      <h3><span>Express</span> Freight</h3>
      <p>Simply dummy text of the printing and typesetting industry.</p>
      <svg width="18" height="14" viewBox="0 0 18 14"><path d="M1 7h15M10 1l6 6-6 6" stroke="var(--red)" stroke-width="2" fill="none"/></svg>
    </article>
    <article class="card">
      <div class="card-photo" role="img" aria-label="Loaded delivery van parked on a city street"></div>
      <h3><span>Express</span> Transported</h3>
      <p>Simply dummy text of the printing and typesetting industry.</p>
      <svg width="18" height="14" viewBox="0 0 18 14"><path d="M1 7h15M10 1l6 6-6 6" stroke="var(--red)" stroke-width="2" fill="none"/></svg>
    </article>
  </div>
</section>

<section class="band">
  <svg class="bg" width="1200" height="86" viewBox="0 0 1200 86">
    <polygon points="485,6 1200,6 1200,86 405,86" fill="var(--navy)"/>
    <polygon points="0,0 485,0 430,80 0,80" fill="var(--red)"/>
  </svg>
  <div class="band-new"><strong>New Customer?</strong><small>Click for information</small></div>
  <div class="band-track"><small>The BLX Online</small><strong>Order &amp; Tracking program</strong></div>
  <div class="band-actions">
    <span>Register</span><span class="or">or</span>
    <span class="btn-login"><svg width="10" height="12" viewBox="0 0 10 12"><rect x="0" y="5" width="10" height="7" fill="#fff"/><path d="M2 5V3a3 3 0 0 1 6 0v2" stroke="#fff" stroke-width="1.6" fill="none"/></svg>Login</span>
  </div>
</section>

<section class="careers">
  <h2 class="section-h">Our <b>Careers</b></h2>
  <ul>
    <li><svg width="14" height="12" viewBox="0 0 14 12"><path d="M1 6l4 4 8-9" stroke="var(--red)" stroke-width="2.2" fill="none"/></svg>Lorem ipsum dolor sit amet, consectetur adipiscing elit.</li>
    <li><svg width="14" height="12" viewBox="0 0 14 12"><path d="M1 6l4 4 8-9" stroke="var(--red)" stroke-width="2.2" fill="none"/></svg>Aenean rutrum elit posuere, rhoncus diam ac, ornare tortor.</li>
    <li><svg width="14" height="12" viewBox="0 0 14 12"><path d="M1 6l4 4 8-9" stroke="var(--red)" stroke-width="2.2" fill="none"/></svg>Aenean sed metus rhoncus, odio et fringilla felis et, fringilla lectus.</li>
    <li><svg width="14" height="12" viewBox="0 0 14 12"><path d="M1 6l4 4 8-9" stroke="var(--red)" stroke-width="2.2" fill="none"/></svg>Etiam dictum sem quis augue vestibulum dapibus.</li>
    <li><svg width="14" height="12" viewBox="0 0 14 12"><path d="M1 6l4 4 8-9" stroke="var(--red)" stroke-width="2.2" fill="none"/></svg>Vivamus euismod est sed diam efficitur rutrum.</li>
    <li><svg width="14" height="12" viewBox="0 0 14 12"><path d="M1 6l4 4 8-9" stroke="var(--red)" stroke-width="2.2" fill="none"/></svg>Nullam ullamcorper mauris vitae nisl viverra, quis condimentum leo condimentum.</li>
    <li><svg width="14" height="12" viewBox="0 0 14 12"><path d="M1 6l4 4 8-9" stroke="var(--red)" stroke-width="2.2" fill="none"/></svg>Fusce tincidunt lacus sit amet justo sagittis commodo.</li>
  </ul>
</section>

<section class="testimonials">
  <h2 class="section-h">Client <b>Testimonials</b></h2>
  <blockquote class="quote">
    <svg width="34" height="28" viewBox="0 0 34 28"><path d="M0 28V14C0 6 4 1 12 0v5c-4 1-6 4-6 8h6v15zM19 28V14c0-8 4-13 12-14v5c-4 1-6 4-6 8h6v15z" fill="#cfcfcf"/></svg>
    “ It is a long established fact that a reader will be distracted by the readable content of a page when looking at its layout. The point of using Lorem Ipsum is that it has a more-or-less normal distribution of letters, as opposed to using...”
  </blockquote>
  <div class="author">
    <div class="author-photo" role="img" aria-label="Client portrait"></div>
    <div class="author-name">Marlon Pike</div>
    <div class="author-place">USA, Detroit</div>
    <div class="author-nav">
      <svg width="10" height="16" viewBox="0 0 10 16"><path d="M8 2L2 8l6 6" stroke="#888" stroke-width="2.4" fill="none"/></svg>
      <svg width="10" height="16" viewBox="0 0 10 16"><path d="M2 2l6 6-6 6" stroke="#888" stroke-width="2.4" fill="none"/></svg>
    </div>
  </div>
</section>

<footer class="site-footer">
  <div class="f-col f-links">
    <h4>Quick Link</h4>
    <ul><li>- Home</li><li>- About Us</li><li>- Freight</li><li>- Courier</li><li>- Transported</li><li>- Careers</li></ul>
  </div>
  <div class="f-col f-news">
    <h4>Join our Newsletter</h4>
    <p>Subscribe to our Newsletter to get the latest scoop right to your inbox</p>
    <div class="field">Enter Your Email</div>
    <div class="submit">Submit</div>
  </div>
  <div class="f-col f-contact">
    <h4>Contact</h4>
    <p>1234 Street Name, City Name, United States</p>
    <p>123-456-7890</p>
    <p>info@brisklark.com</p>
    <div class="socials">
      <span style="background:#55555f"></span><span style="background:#55555f"></span><span style="background:#55555f"></span><span style="background:#55555f"></span>
    </div>
  </div>
  <div class="f-col f-map" role="img" aria-label="Street map showing the office location"></div>
  <span class="f-map-link">View full Map</span>
</footer>

<div class="legal">
  <span class="copy">© 2016 Brisk Lark Express Delivery, All Rights Reserved</span>
  <span class="links">Sitemap &nbsp;|&nbsp; Contact Us</span>
</div>

</body>
</html>
```